Business Card Design

Rubber roller servicing company. Specializing in rubber to metal bonding. Serving various industries including, pharmaceutical, textile, plastic extrusion, polythene bag converting, laminating and the food industries.

Industry/Entity Type

Plastic

Contact Information for Business Card

Carwick Roller & Rubber Co Ltd, Trevor Ambleside, Managing Director, Unit at Fernholt, Ridley Lane, Oxenby, Huddersfield, North Wendale, HX4 9TJ, Tel 01632 960481, Fax 01632 960527, email info@carwickroller.example.co.uk,

```html
<!DOCTYPE html>
<html lang="en">
<head>
<meta charset="utf-8">
<title>Carwick Roller &amp; Rubber Co Ltd — Business Card</title>
<link rel="stylesheet" href="https://fonts.googleapis.com/css2?family=Arimo:wght@400;700&display=swap">
<style>
  :root {
    --page-bg: #ffffff;
    --card-bg: #58c9e2;
    --card-edge: #d6ecf2;
    --text-light: #ffffff;
    --text-dark: #2f3a3f;
    --icon-dark: #1f2a2e;
  }
  * { margin: 0; padding: 0; box-sizing: border-box; }
  html, body {
    width: 1200px; height: 901px; overflow: hidden;
    background: var(--page-bg);
    font-family: "Arimo", Arial, sans-serif;
  }
  .card {
    position: absolute; left: 150px; top: 178px;
    width: 900px; height: 545px;
    background: var(--card-bg);
    border: 1px solid var(--card-edge);
  }
  .person { position: absolute; left: 56px; top: 66px; color: var(--text-light); }
  .person-name { font-size: 34px; font-weight: 400; letter-spacing: 0.3px; }
  .person-role { font-size: 21px; font-weight: 400; margin-top: 8px; margin-left: 12px; }
  .company {
    position: absolute; right: 46px; top: 92px;
    text-align: right; color: var(--text-light);
    font-weight: 700;
  }
  .company-name { display: block; font-size: 72px; line-height: 1; letter-spacing: 1px; }
  .company-type { display: block; font-size: 38px; line-height: 1.1; margin-top: -4px; }
  .contacts { position: absolute; left: 60px; top: 300px; list-style: none; color: var(--text-dark); }
  .contact {
    display: flex; align-items: flex-start;
    font-size: 20px; line-height: 30px; margin-bottom: 18px;
  }
  .contact-icon { width: 28px; height: 28px; margin-right: 28px; flex: none; }
  .contact-icon svg { width: 28px; height: 28px; fill: var(--icon-dark); }
  .contact-address { line-height: 36px; margin-top: -2px; }
</style>
</head>
<body>
  <section class="card">
    <div class="person">
      <div class="person-name">Trevor Ambleside</div>
      <div class="person-role">Managing Director</div>
    </div>

    <div class="company">
      <span class="company-name">CARWICK</span>
      <span class="company-type">roller &amp; rubber co ltd.</span>
    </div>

    <ul class="contacts">
      <li class="contact">
        <span class="contact-icon"><svg viewBox="0 0 24 24" aria-hidden="true"><path d="M6.6 10.8a15 15 0 0 0 6.6 6.6l2.2-2.2c.3-.3.7-.4 1-.2 1.1.4 2.3.6 3.6.6.6 0 1 .4 1 1V20c0 .6-.4 1-1 1A17 17 0 0 1 3 4c0-.6.4-1 1-1h3.5c.6 0 1 .4 1 1 0 1.3.2 2.5.6 3.6.1.3 0 .7-.2 1z"/></svg></span>
        <span>01632 960481</span>
      </li>
      <li class="contact">
        <span class="contact-icon"><svg viewBox="0 0 24 24" aria-hidden="true"><path d="M7 3h10v4H7zM4 8h16a2 2 0 0 1 2 2v6h-4v5H6v-5H2v-6a2 2 0 0 1 2-2zm4 8v3h8v-3zm0 1h8v.8H8zm10-6.5a1 1 0 1 0 0 2 1 1 0 0 0 0-2z"/></svg></span>
        <span>01632 960527</span>
      </li>
      <li class="contact">
        <span class="contact-icon"><svg viewBox="0 0 24 24" aria-hidden="true"><path d="M2 5h20v14H2zm2 2v10h16V7l-8 6zm1.5 0L12 11.8 18.5 7z" fill-rule="evenodd"/></svg></span>
        <span>info@carwickroller.example.co.uk</span>
      </li>
      <li class="contact">
        <span class="contact-icon"><svg viewBox="0 0 24 24" aria-hidden="true"><path d="M12 2a7 7 0 0 0-7 7c0 5 7 13 7 13s7-8 7-13a7 7 0 0 0-7-7zm0 4a3 3 0 1 1 0 6 3 3 0 0 1 0-6z"/></svg></span>
        <span class="contact-address">Unit at Fernholt, Ridley Lane, Oxenby,<br>Brackleigh, North Wendale, HX4 9TJ</span>
      </li>
    </ul>
  </section>
</body>
</html>
```